Boracay Wedding Invitation Design

Hello, We would like a wedding invitation design for our wedding in Boracay. We would like it somewhat in the form of a boarding pass with beachy fresh colours, possibly a nice Boracay beach in the background Double sided with an envelope design to match. Maybe something simple on the envelope like a nice picture in the bottom left corner of a shell on a beach or something similar.

I would also like on the opposite side of the invite to be an "information sheet" with a matching beach design

The text files for both sides are included and i have also included 2 designs that i thought looked nice and are similar to what we are after.
Updates

Hello, I have updated the brief to be more specific with text files and images to make it easier for you. Thank you :)

Industry/Entity Type

Wedding

Font styles to use
Decorative
Script

Colors
fbee3d
33a6d7
33b8a4
fbf289
85cae6
ffffff

Requirements
Must have
• I would like to have this quote somewhere on the invitation
• This day I will marry my best friend,
• the one I laugh with,
• live for,
• dream with,
• love
• Owen & Marisa
• Request the pleasure of your company to celebrate their wedding
• On Friday the 17th March 2017
• at
• Velunda Grand Suites
• Boracay, Philippines
• Ceremony begins at 3.00pm
• RSVP
• Owen 0431907254
• Marisa 0417283649
• by
• 17th Jan 2016
• Dress: Beach Formal
• For the "information sheet"
• There will be a 5% discount on rooms booked at the Velunda under the event Owen & Marisa Wedding. The resort has a total of 24 rooms it would be nice if the majority of guests could stay at the resort from the night before until the night after the wedding but if you choose to stay elsewhere on the island there are plenty of other places to stay for cheaper and everything is fairly close as its a small island.
• We have currently blocked room stay for a short period of time so our guests can book rooms. If you choose to do so please email reservations@velundastays.example. Once rooms become available to the public again, towards the end of Jan, it will be first come first served basis. The resort is very popular so im assuming once this happens the rooms will be booked out.
• If you would like to check out the resort itself the website is www.velundagrand-isle.example
• We know its a fair distance to travel but we would really love to see you all there to celebrate and maybe even enjoy a small holiday while your here its a beautiful part of the world.
• If anyone has any questions please feel free to contact Owen on 0431907254
Nice to have
• A nice picture of a Boracay beach in the background would be nice

```html
<!DOCTYPE html>
<html lang="en">
<head>
<meta charset="utf-8">
<title>Owen &amp; Marisa – Boarding Pass Wedding Invitation</title>
<link href="https://fonts.googleapis.com/css2?family=Kalam&family=Kaushan+Script&family=Caveat+Brush&family=Cormorant+SC:wght@700&family=Oswald:wght@400&family=PT+Sans+Narrow&family=Poiret+One&family=Parisienne&family=Josefin+Sans:wght@400&family=Courier+Prime&display=swap" rel="stylesheet">
<style>
  :root {
    --backdrop: #2f64b8;
    --card: #dfe6cf;
    --ink: #1e1e1e;
    --muted: #6b6b6b;
    --orange: #f0822f;
    --sand: #e2c79b;
    --sand-light: #efdcb8;
    --sea: #6fb3c4;
    --sky: #7fb6e6;
    --aqua: #a9e1ef;
    --aqua-mid: #7fd0ec;
    --aqua-deep: #48b6e6;
  }
  * { margin: 0; padding: 0; box-sizing: border-box; }
  html, body { width: 1200px; height: 1200px; overflow: hidden; }
  body { background: var(--backdrop); position: relative; color: var(--ink); }

  .card { position: absolute; left: 53px; width: 1104px; height: 484px; background: var(--card); overflow: hidden; }
  .card--invite { top: 78px; }
  .card--details { top: 618px; }

  .art { position: absolute; }
  .vertical { position: absolute; writing-mode: vertical-rl; transform: rotate(180deg); white-space: nowrap; line-height: 1; }

  /* front stub */
  .stub-title { left: 28px; bottom: 86px; font-family: "Poiret One", sans-serif; font-size: 33px; letter-spacing: 6px; color: var(--muted); }
  .stub-names { left: 66px; bottom: 34px; font-family: "Josefin Sans", sans-serif; font-size: 25px; letter-spacing: 0.5px; }
  .stub-date { left: 66px; top: 32px; font-family: "Courier Prime", monospace; font-size: 24px; letter-spacing: 2px; }

  .beach-art { left: 117px; top: 0; width: 317px; height: 484px; background: linear-gradient(100deg, var(--sand) 0%, var(--sand-light) 45%, #d9e2d9 60%, var(--sea) 100%); }
  .quote { position: absolute; left: 167px; top: 132px; font-family: "Kalam", cursive; font-size: 22px; line-height: 37.5px; }

  .photo { left: 434px; top: 0; width: 670px; height: 484px; background: linear-gradient(180deg, var(--sky) 0%, #b8d8ee 25%, #5a6e5a 30%, #8ccfd4 45%, #cfe9e6 60%, #f1ece0 80%, #e6dccb 100%); }
  .couple { position: absolute; left: 590px; top: 132px; font-family: "Kaushan Script", cursive; font-size: 54px; font-weight: 400; color: var(--orange); }

  .invite-panel { position: absolute; left: 487px; top: 215px; width: 567px; height: 247px; background: var(--card); border-radius: 16px; }
  .invite-line { position: absolute; left: 0; width: 100%; top: 12px; text-align: center; font-family: "Cormorant SC", serif; font-weight: 700; font-size: 22px; line-height: 27px; }
  .date-pill { position: absolute; left: 80px; top: 73px; width: 387px; height: 42px; border-radius: 21px; background: var(--orange); color: #fff; text-align: center; font-family: "Oswald", sans-serif; font-size: 25px; line-height: 42px; }
  .venue-label { position: absolute; left: 47px; top: 132px; font-family: "PT Sans Narrow", sans-serif; font-size: 21px; letter-spacing: 0.5px; }
  .venue { position: absolute; left: 47px; top: 158px; font-family: "Caveat Brush", cursive; font-size: 23px; line-height: 23px; color: var(--orange); letter-spacing: 1.5px; }
  .rsvp { position: absolute; left: 358px; top: 127px; font-family: "PT Sans Narrow", sans-serif; font-size: 17.5px; line-height: 20px; }
  .phone { display: inline-block; vertical-align: -2px; margin: 0 2px; }
  .attire { color: var(--orange); margin-top: 7px; display: block; }

  /* back */
  .strip-left { left: 0; top: 0; width: 47px; height: 484px; background: linear-gradient(180deg, #7fb9cf, var(--sand) 35%, #bfdbe6 60%, var(--sand) 100%); }
  .strip-right { left: 105px; top: 0; width: 52px; height: 484px; background: linear-gradient(180deg, var(--sand) 0%, var(--sand-light) 50%, var(--sand) 100%); }
  .back-stub-date { left: 66px; top: 32px; font-family: "Courier Prime", monospace; font-size: 20px; letter-spacing: 2px; }
  .back-stub-names { left: 56px; bottom: 57px; font-family: "Josefin Sans", sans-serif; font-size: 23px; letter-spacing: 0.5px; }

  .heading-the { position: absolute; left: 177px; top: 55px; font-family: "Parisienne", cursive; font-size: 58px; color: var(--orange); }
  .heading-details { position: absolute; left: 308px; top: 55px; font-family: "Poiret One", sans-serif; font-weight: 400; font-size: 62px; letter-spacing: 9px; color: var(--ink); }
  .subheading { position: absolute; left: 215px; top: 128px; font-family: "Josefin Sans", sans-serif; font-size: 24px; letter-spacing: 2px; }
  .body-copy { position: absolute; left: 203px; top: 197px; width: 405px; font-family: "PT Sans Narrow", sans-serif; font-size: 18.5px; line-height: 25px; }
  .shell-art { left: 258px; top: 382px; width: 250px; height: 90px; border-radius: 45px; background: radial-gradient(ellipse at center, #f2c48a 0%, rgba(223,230,207,0) 70%); }

  .note { position: absolute; left: 667px; width: 415px; border-radius: 14px; padding: 4px 22px 4px 21px; font-family: "PT Sans Narrow", sans-serif; font-size: 18px; line-height: 22.5px; box-shadow: 8px 8px 10px rgba(0,0,0,0.25); }
  .note--block { top: 57px; height: 162px; background: var(--aqua); }
  .note--site { top: 234px; height: 58px; background: var(--aqua-mid); padding-top: 6px; }
  .note--welcome { top: 304px; height: 123px; background: var(--aqua-deep); padding-top: 6px; }
</style>
</head>
<body>

<section class="card card--invite">
  <div class="art beach-art" role="img" aria-label="Illustrated beach with sand, shells, starfish and flip-flops at the shoreline"></div>
  <div class="vertical stub-title">BOARDINGPASS</div>
  <div class="vertical stub-names">OWEN + MARISA</div>
  <div class="vertical stub-date">03. 17. 2016</div>
  <p class="quote">This day I will marry<br>my best friend,<br>the one I laugh with,<br>live for,<br>dream with,<br>Love</p>

  <div class="art photo" role="img" aria-label="Photograph of a tropical beach with rock islets, palm trees and outrigger boats in clear water"></div>
  <h1 class="couple">Owen &amp; Marisa</h1>

  <div class="invite-panel">
    <p class="invite-line">Request the Pleasure Of Your Company<br>To Celebrate Their Wedding</p>
    <p class="date-pill">FRIDAY,&nbsp; MARCH 17, 2017 AT 3 PM</p>
    <p class="venue-label">CEREMONY &amp; RECEPTION</p>
    <p class="venue">VELUNDA GRAND SUITES<br>BORACAY ISLAND,<br>PHILIPPINES</p>
    <p class="rsvp">RSVP<br>
      Owen <svg class="phone" width="16" height="16" viewBox="0 0 16 16"><circle cx="8" cy="8" r="7" fill="none" stroke="#1e1e1e" stroke-width="1.2"/><path d="M5.5 4.5c-.6.6-.5 2 .8 3.8s2.8 2.8 3.6 2.4l.8-.8-1.4-1.2-.8.5c-.6-.3-1.4-1.2-1.7-1.8l.5-.8-1.1-1.5z" fill="#1e1e1e"/></svg> 0431907254<br>
      Marisa <svg class="phone" width="16" height="16" viewBox="0 0 16 16"><circle cx="8" cy="8" r="7" fill="none" stroke="#1e1e1e" stroke-width="1.2"/><path d="M5.5 4.5c-.6.6-.5 2 .8 3.8s2.8 2.8 3.6 2.4l.8-.8-1.4-1.2-.8.5c-.6-.3-1.4-1.2-1.7-1.8l.5-.8-1.1-1.5z" fill="#1e1e1e"/></svg> 0417283649<br>
      by 17th Jan 2016
      <span class="attire">Attire: Beach Formal</span>
    </p>
  </div>
</section>

<section class="card card--details">
  <div class="art strip-left" role="img" aria-label="Strip of beach illustration with sea urchin shell and flip-flops"></div>
  <div class="vertical back-stub-date">03. 17. 2016</div>
  <div class="vertical back-stub-names">OWEN + MARISA</div>
  <div class="art strip-right" role="img" aria-label="Strip of sandy beach illustration with shells"></div>

  <span class="heading-the">the</span>
  <h2 class="heading-details">DETAILS</h2>
  <p class="subheading">HOTEL INFORMATION</p>
  <p class="body-copy">There will be a 5% discount on rooms booked at the Velunda under the event Owen &amp; Marisa Wedding. The resort has a total of 24 rooms it would be nice if the majority of guests could stay at the resort from the night before until the night after the wedding but if you choose to stay elsewhere on the island there are plenty of other places to stay for cheaper and everything is fairly close as its a small island.</p>
  <div class="art shell-art" role="img" aria-label="Illustrated seashells and a red starfish"></div>

  <p class="note note--block">We have currently blocked room stay for a short period of time so our guests can book rooms. If you choose to do so please email reservations@velundastays.example. Once rooms become available to the public again, towards the end of January, it will be first come first served basis. The resort is very popular so im assuming once this happens the rooms will be booked out.</p>
  <p class="note note--site">If you would like to check out the resort itself the website is www.velundagrand-isle.example</p>
  <p class="note note--welcome">We know its a fair distance to travel but we would really love to see you all there to celebrate and maybe even enjoy a small holiday while your here its a beautiful part of the world.- If anyone has any questions please feel free to contact Owen on <svg class="phone" width="16" height="16" viewBox="0 0 16 16"><circle cx="8" cy="8" r="7" fill="none" stroke="#1e1e1e" stroke-width="1.2"/><path d="M5.5 4.5c-.6.6-.5 2 .8 3.8s2.8 2.8 3.6 2.4l.8-.8-1.4-1.2-.8.5c-.6-.3-1.4-1.2-1.7-1.8l.5-.8-1.1-1.5z" fill="#1e1e1e"/></svg> 0431907254.</p>
</section>

</body>
</html>
```